New Poster Design Project

Make an out standing A2 poster with below information,it is out first edition!Use the Attached image as background,Thanx!

Tolvik Meridian Arts Gathering
16 - 22 June 2014
Www.tmagfest.example

Creating a new vision of Africa through African Arts and Culture

Guest speakers / Artists

Delphine Korrato-Væstrup (S.A)
Tekle Berhanu Woldesan (Ethio)
Ronny Bastien-Kolo (Uganda)
Håkon Lunde (Nor)
Velvet Drum Collective (Zim)
Kalumbero Band (Moz,Nor,Swe & Zim)
Dj Zoto Zoto with Afro beats (Ghana/UK )
Dj Marquee/Storm Duchess with collage mix (Bergen)

@ Cafe Lutembe, Nordvik Global Heritage House (Nghh) Helsebrygga,Kjøpmannsplassen,Lindehagen & Vevergangen gate

Mon-Thur
Free entry,food & drinks served

Fri - Entry by donation & Sat - Tmagfest closing ceremony (100kr)
Updates

Project Deadline Extended

Project Deadline Extended
Reason: I made a mistake on extending time on this project now I can not reverse the extended time aaarrrr!!!I really dont have time,The poster should be all over the place by now since Im left with a couple of days away to the festival!!!I need someone to QuickFix me a A2 top notch poster in No time...my deadline is NOW NOW,LATEST Wednesday 21 May 2014,Thanx!

Industry/Entity Type

Cafe

Requirements
Must have
• sponsors logo
Nice to have
• Symbols
Should not have

```html
<!DOCTYPE html>
<html lang="en">
<head>
<meta charset="utf-8">
<title>Tolvik Meridian Arts Gathering</title>
<link rel="stylesheet" href="https://fonts.googleapis.com/css2?family=Questrial&family=PT+Sans+Narrow:wght@400;700&family=Ubuntu+Condensed&display=swap">
<style>
  :root {
    --page: #fdfde9;
    --dark: #141210;
    --olive: #bfbf78;
    --blue: #5b7fa6;
    --rust: #c4552a;
    --ink: #111111;
    --white: #ffffff;
  }
  * { margin: 0; padding: 0; box-sizing: border-box; }
  html, body { width: 1200px; height: 1200px; overflow: hidden; background: var(--page); }
  .canvas { position: relative; width: 1200px; height: 1200px; }
  .poster {
    position: absolute; left: 258px; top: 104px; width: 703px; height: 992px;
    background: var(--white); overflow: hidden;
    font-family: "PT Sans Narrow", sans-serif;
  }
  .photo-panel {
    position: absolute; left: 0; top: 0; width: 380px; height: 869px;
    background: radial-gradient(ellipse at 45% 60%, #6b5a4c 0%, #3a302a 45%, var(--dark) 80%);
  }
  .olive-panel {
    position: absolute; left: 380px; top: 0; width: 323px; height: 869px;
    background: var(--olive);
  }
  .figure-silhouettes {
    position: absolute; left: 565px; top: 575px; width: 120px; height: 230px;
    background: rgba(255,255,255,0.22); border-radius: 60px 60px 20px 20px;
  }
  .wordmark {
    position: absolute; left: 12px; top: 0; color: var(--blue);
    font-family: "Questrial", sans-serif; white-space: nowrap; line-height: 1;
  }
  .wordmark .initial { font-size: 330px; vertical-align: top; display: inline-block; margin-top: -20px; }
  .wordmark .rest { font-size: 170px; vertical-align: top; display: inline-block; margin-top: -8px; margin-left: -14px; }
  .rule { position: absolute; left: 136px; top: 154px; width: 530px; height: 4px; background: var(--rust); }
  .info { position: absolute; left: 380px; width: 323px; text-align: center; line-height: 1.1; }
  .event-name { top: 178px; font-weight: 700; font-size: 29px; color: var(--ink); }
  .dates { top: 218px; font-weight: 700; font-size: 23px; color: var(--white); }
  .site { top: 248px; font-weight: 700; font-size: 23px; color: var(--rust); }
  .tagline { top: 282px; font-weight: 700; font-size: 25px; color: var(--ink); line-height: 1.15; }
  .speakers-band {
    position: absolute; left: 325px; top: 377px; width: 378px; height: 48px;
    background: var(--blue); color: var(--white); font-weight: 700; font-size: 34px;
    text-align: center; line-height: 48px;
  }
  .lineup { top: 438px; list-style: none; font-family: "Ubuntu Condensed", sans-serif; font-size: 16px; line-height: 24px; color: var(--white); }
  .venues { top: 678px; font-weight: 700; font-size: 21px; line-height: 25px; color: var(--rust); }
  .schedule { top: 776px; font-weight: 700; font-size: 21px; line-height: 27px; color: var(--ink); }
  .schedule .friday { margin-top: 6px; }
  .saturday-band {
    position: absolute; left: 22px; top: 869px; width: 681px; height: 32px;
    background: var(--rust); color: var(--white); font-weight: 700; font-size: 18px;
    text-align: center; line-height: 32px;
  }
  .sponsors { position: absolute; left: 0; top: 906px; width: 703px; text-align: center; }
  .sponsors-title { font-family: "Ubuntu Condensed", sans-serif; font-size: 15px; color: var(--ink); }
  .sponsor-row { display: flex; justify-content: center; align-items: center; gap: 12px; margin-top: 12px; }
  .sponsor { display: flex; align-items: center; gap: 3px; font-family: "Ubuntu Condensed", sans-serif; font-size: 10px; color: #333; white-space: nowrap; }
  .sponsor .dot { width: 14px; height: 14px; border-radius: 50%; background: var(--blue); }
</style>
</head>
<body>
<div class="canvas">
  <div class="poster">
    <div class="photo-panel" role="img" aria-label="Sepia photograph of a smiling woman in a white head wrap leaning on a carved thumb piano, with a carved mask shape beside her"></div>
    <div class="olive-panel"></div>
    <div class="figure-silhouettes" role="img" aria-label="Faint silhouettes of women carrying baskets and a decorative mask motif"></div>

    <h1 class="wordmark"><span class="initial">T</span><span class="rest">olvik</span></h1>
    <div class="rule"></div>

    <p class="info event-name">Meridian Arts Gathering</p>
    <p class="info dates">16-22 June 2014</p>
    <p class="info site">www.tmagfest.example</p>
    <p class="info tagline">A new vision of Africa<br>through<br>African Arts and Culture</p>

    <h2 class="speakers-band">Guest Speakers/Artists</h2>
    <ul class="info lineup">
      <li>Delphine Korrato-Væstrup (SA)</li>
      <li>Tekle Berhanu Woldesan (Ethio)</li>
      <li>Ronny Bastien-Kolo (Uganda)</li>
      <li>Håkon Lunde (Nor)</li>
      <li>Velvet Drum Collective (Zim)</li>
      <li>Kalumbero Band (Moz,Nor,Swe &amp; Zim)</li>
      <li>Dj Zoto Zoto with Afro beats (Ghana/UK)</li>
      <li>Dj Marquee/Storm Duchess with</li>
      <li>collage mix (Bergen)</li>
    </ul>

    <p class="info venues">@Cafe Lutembe, Nordvik<br>Global Heritage House (Nghh)<br>Helsebrygga, Kjøpmannsplassen<br>Lindehagen &amp; Vevergangen gate</p>

    <div class="info schedule">
      <p>Mon - Thur</p>
      <p>Free entry, food &amp; drinks</p>
      <p class="friday">Friday-All Africa music mix</p>
    </div>

    <p class="saturday-band">Saturday noon - Market, Carnival, Workshops + Evening Concert &amp; Djing 21:00 (100kr)</p>

    <div class="sponsors">
      <p class="sponsors-title">Supported By:</p>
      <div class="sponsor-row">
        <span class="sponsor">Kora Circle</span>
        <span class="sponsor">lampehuset.example</span>
        <span class="sponsor">Ruta Arts</span>
        <span class="sponsor"><span class="dot"></span>Nordvik Kommune</span>
        <span class="sponsor">vrk.example</span>
        <span class="sponsor"><span class="dot"></span></span>
        <span class="sponsor">Living Well Forum</span>
        <span class="sponsor">Elvo</span>
        <span class="sponsor">Sabe</span>
        <span class="sponsor">Frivoll</span>
      </div>
    </div>
  </div>
</div>
</body>
</html>
```